Upsell Vertical Banner Ad Design For B2B Marketing Agency Vertical 768px × 1180px IS THE SIZE

I need a banner made for my website www.brightlanepromotionhub.biz This banner will be an upsell advertisement for after someone signs up for my monthly program. When they login to their account for the 1st time I will give them the chance to upgrade their account to our annual program with just one click.

this is a page that upsells it currently to give you an idea how we market ourselves:
https://tlpx.pagevault-example.com/page/tlp-annual-upsell

Use this content:

Are You Ready To Commit To Taking Your Business To The Next Level?

Because We're In This For The Long-Haul and Dedicated To Your Success...

Save $300 By Upgrading To An Annual Membership And Pay Only $74/mth

((BUTTON))Yes, Upgrade My Plan Right Now!

*Must prepay the full year at only $898/yr!

Target Market(s)

business owners

Industry/Entity Type

Marketing

Requirements
Must have
• 768px × 1180px IS THE SIZE vertical

Use this content:

Nice to have
• Use this content:

Should not have
• Use this content:

```html
<!DOCTYPE html>
<html lang="en">
<head>
<meta charset="utf-8">
<title>Brightlane Promotion Hub – Annual Upsell Banners</title>
<link href="https://fonts.googleapis.com/css2?family=Roboto:wght@300;400;500;700&display=swap" rel="stylesheet">
<style>
  :root {
    --board: #333333;
    --panel-light: #e9e7eb;
    --brand-blue: #1570bd;
    --brand-teal: #00b8c2;
    --ink: #222222;
    --green-top: #58b05a;
    --green-bottom: #4aa64d;
    --white: #ffffff;
    --photo-light: #ece9ec;
    --photo-mid: #d9d3cf;
  }
  * { box-sizing: border-box; margin: 0; padding: 0; }
  html, body { width: 1200px; height: 925px; overflow: hidden; }
  body {
    background: var(--board);
    font-family: "Roboto", Arial, sans-serif;
    position: relative;
  }
  .banner {
    position: absolute;
    top: 67px;
    width: 768px;
    height: 1180px;
    transform-origin: 0 0;
    transform: scale(0.6704);
    overflow: hidden;
  }
  .banner--light { left: 68px; background: var(--panel-light); }
  .banner--green { left: 617px; }

  .brand {
    position: absolute;
    left: 0; right: 0;
    top: 44px;
    display: flex;
    justify-content: center;
    align-items: center;
    gap: 14px;
    font-weight: 500;
    font-size: 34px;
    letter-spacing: 1px;
  }
  .brand__dot { width: 22px; height: 22px; border-radius: 50%; }
  .banner--light .brand { color: var(--brand-blue); }
  .banner--light .brand__dot { background: var(--brand-blue); }
  .banner--green .brand { color: var(--white); top: 48px; }
  .banner--green .brand__dot { background: var(--white); }

  /* Light banner cards */
  .cards {
    position: absolute;
    top: 142px; left: 49px;
    display: flex; gap: 13px;
  }
  .card {
    width: 217px; height: 286px;
    border-radius: 18px;
    background: var(--brand-blue);
    color: var(--white);
    font-size: 23px;
    line-height: 30px;
    text-align: center;
    padding: 50px 14px 0;
  }
  .card--teal { background: var(--brand-teal); }

  .cta {
    position: absolute;
    left: 49px; width: 677px; height: 68px;
    display: flex; align-items: center; justify-content: center;
    color: var(--white);
    font-weight: 700; font-size: 20px;
    border-radius: 3px;
    box-shadow: 0 3px 6px rgba(0,0,0,0.2);
  }
  .banner--light .cta { top: 455px; background: var(--brand-teal); }
  .banner--green .cta { top: 1050px; left: 46px; background: var(--brand-blue); }

  .offer {
    position: absolute; left: 0; right: 0;
    text-align: center;
  }
  .offer__lead { font-size: 35px; font-weight: 500; line-height: 42px; }
  .offer__line { font-size: 35px; font-weight: 300; line-height: 44px; }
  .offer__price { font-size: 62px; font-weight: 700; line-height: 80px; }
  .banner--light .offer { top: 552px; color: var(--ink); }
  .banner--light .offer__price { color: var(--brand-blue); }
  .banner--green .offer { top: 847px; color: var(--white); }

  .photo-woman {
    position: absolute; left: 0; right: 0; top: 700px; bottom: 0;
    background: linear-gradient(180deg, var(--panel-light) 0%, var(--photo-light) 30%, var(--photo-mid) 100%);
  }
  .photo-team {
    position: absolute; inset: 0;
    background: linear-gradient(160deg, var(--green-top) 0%, var(--green-bottom) 100%);
  }

  .hex {
    position: absolute;
    width: 320px; height: 380px;
  }
  .hex svg.hex__shape { position: absolute; inset: 0; }
  .hex__icon { position: absolute; left: 115px; width: 90px; height: 90px; }
  .hex__text {
    position: absolute; left: 20px; right: 20px;
    color: var(--white);
    font-size: 23px; line-height: 30px;
    text-align: center;
  }
</style>
</head>
<body>

  <section class="banner banner--light">
    <div class="photo-woman" role="img" aria-label="Photo of a happy young woman sitting cross-legged with a laptop, arms raised, beside a potted plant and books"></div>
    <div class="brand"><span class="brand__dot"></span>BRIGHTLANE PROMOTION HUB</div>
    <div class="cards">
      <div class="card">Are You Ready To Commit To Taking Your Business To The Next Level?</div>
      <div class="card card--teal">Because We're In This For The Long-Haul and Dedicated To Your Success...</div>
      <div class="card">Save $300 By Upgrading To An Annual Membership And Pay Only $74/mth</div>
    </div>
    <div class="cta">YES, UPGRADE MY PLAN RIGHT NOW!</div>
    <div class="offer">
      <p class="offer__lead">*Must prepay</p>
      <p class="offer__line">the full year at only</p>
      <p class="offer__price">$898/yr!</p>
    </div>
  </section>

  <section class="banner banner--green">
    <div class="photo-team" role="img" aria-label="Green-tinted photo of business people meeting around a table"></div>
    <div class="brand"><span class="brand__dot"></span>BRIGHTLANE PROMOTION HUB</div>

    <div class="hex" style="left:52px; top:128px;">
      <svg class="hex__shape" viewBox="0 0 320 380"><polygon points="160,0 320,95 320,285 160,380 0,285 0,95" fill="var(--brand-blue)"/></svg>
      <svg class="hex__icon" style="top:62px" viewBox="0 0 90 90" fill="none" stroke="#fff" stroke-width="3">
        <rect x="16" y="44" width="58" height="36" rx="3"/>
        <line x1="6" y1="82" x2="84" y2="82"/>
        <path d="M24 36 a21 21 0 0 1 42 0"/>
        <rect x="18" y="32" width="8" height="14" rx="2"/>
        <rect x="64" y="32" width="8" height="14" rx="2"/>
        <circle cx="45" cy="62" r="4"/>
      </svg>
      <p class="hex__text" style="top:180px">Are You Ready To Commit To Taking Your Business To The Next Level?</p>
    </div>

    <div class="hex" style="left:397px; top:128px;">
      <svg class="hex__shape" viewBox="0 0 320 380"><polygon points="160,0 320,95 320,285 160,380 0,285 0,95" fill="var(--brand-blue)"/></svg>
      <svg class="hex__icon" style="top:66px" viewBox="0 0 90 90" fill="none" stroke="#fff" stroke-width="3">
        <path d="M45 4 a16 16 0 0 1 9 29 v8 h-18 v-8 a16 16 0 0 1 9 -29 z"/>
        <circle cx="45" cy="20" r="5"/>
        <line x1="45" y1="41" x2="45" y2="54"/>
        <circle cx="15" cy="64" r="6"/><path d="M5 86 a10 10 0 0 1 20 0 z"/>
        <circle cx="45" cy="64" r="6"/><path d="M35 86 a10 10 0 0 1 20 0 z"/>
        <circle cx="75" cy="64" r="6"/><path d="M65 86 a10 10 0 0 1 20 0 z"/>
        <line x1="21" y1="60" x2="39" y2="60"/><line x1="51" y1="60" x2="69" y2="60"/>
      </svg>
      <p class="hex__text" style="top:185px">Because We're In This For The Long-Haul and Dedicated To Your Success...</p>
    </div>

    <div class="hex" style="left:226px; top:430px;">
      <svg class="hex__shape" viewBox="0 0 320 380"><polygon points="160,0 320,95 320,285 160,380 0,285 0,95" fill="var(--brand-blue)"/></svg>
      <svg class="hex__icon" style="top:54px" viewBox="0 0 90 90" fill="none" stroke="#fff" stroke-width="3">
        <path d="M34 6 h20 l10 18 v58 a4 4 0 0 1 -4 4 h-32 a4 4 0 0 1 -4 -4 v-58 z" transform="rotate(-12 45 45)"/>
        <path d="M56 14 l18 8 l8 20 l-18 40" />
        <circle cx="42" cy="22" r="4"/>
        <text x="34" y="66" fill="#fff" stroke="none" font-family="Roboto, sans-serif" font-size="24" font-weight="700">$</text>
      </svg>
      <p class="hex__text" style="top:165px">Save $300 By Upgrading To An Annual Membership And Pay Only $74/mth</p>
    </div>

    <div class="offer">
      <p class="offer__lead">*Must prepay</p>
      <p class="offer__line">the full year at only</p>
      <p class="offer__price">$898/yr!</p>
    </div>
    <div class="cta">YES, UPGRADE MY PLAN RIGHT NOW!</div>
  </section>

</body>
</html>
```